7 Herons Distillery - Bottle Label Design

We are a small craft distillery whose branding needs to incorporate our location on a lake (Lac Vernisse, Quebec, Canada). A unique aspect of the lake is that people drive floating docks on the lake powered by a small outboard motor (see photos). Back in the 1970’s when Lac Vernisse was a sparsely populated and difficult-to-access lake in the Gatineau Hills north of Ottawa, the concept of motorized docks was conjured on a lazy afternoon and this single stroke of genius has inadvertently spawned the most exceptional and eccentric lake based community. Throughout the summer, somewhere around four o’clock on any given Friday and Saturday it starts to happen. Docks set sail from their customary landing places - family, friends, snacks and loaded drink coolers in-tow and, as if magnetically drawn, head toward Pine Shoal. Without fail they will come upon a gathering of similar minded floating docks within the vicinity - be guided in with help to moor alongside and within seconds be seamlessly immersed in the festivities. Seldom any longer are these events planned, they have become elemental, a thing organically derived from within the community. This on-going weekly event is the genesis of the strong bond that brings us Seven Herons Distilling.
Each of the 4 distillery owners have one of these docks so hence the name. We are open to either "7 Herons" or spelled out as "Seven Herons" as may be visually appropriate. We are also open to "Distillery" or "Distilling". More detail on the docks themselves, they are 14x16 feet powered by a small outboard motor as shown in the photos. This dock aspect may be difficult to incorporate into the branding but the lake outline is included as an image applicable to include for that local reference aspect. We will be creating very high quality small batch liquors such as vodka, rum, gin and whiskey. Each batch will be triple distilled and perhaps 20 bottles in quantity so very exclusive. We are aiming at a premium feel for the branding. Attached are some bottle label designs that evoke the type of feel we are going for and a photo of the style of blank bottle to design for which is a 750ml Nordic pattern bottle.
In general we are going for more contemporary than traditional, more bold than delicate. If a single label the size desired would be 4 inches wide and 4 inches tall. If a double/split label as in two of the photos the top label would be 3 inches wide and 3 inches tall and the bottom label would be max 4 inches wide and 1.5 inches tall. We are open to the upper label being a "transparent" label to create a printed on bottle effect, perhaps of the brand logo. We are only interested in front label so do not require a back, neck or closure label. The label will require the ability to name the batch style name (example "Tuberix") and then the amplifying information for the type of alcohol (Russian Potato Vodka) in a smaller font. Another example ("Red Fox" and "London Dry Gin"). Information for bottle size (750ml) and alcohol % (40%) are also to be included. Governmental safety warnings are not required. We are open to use of any colours in the label. The basic label design would be re-used for different types of batches where we would change the style and alcohol name.
Updates

Target Market(s)

Up scale premium spirits buyers

Font styles to use
Serif
Sans Serif

Requirements
Must have
• A visual reference to the docks or the lake per the images attached.
Nice to have
• Ideally we can re-use the label design for a different type of Alcohol by changing the alcohol name and style information and maybe the colour of a major element in the label.

```html
<!DOCTYPE html>
<html lang="en">
<head>
<meta charset="utf-8">
<title>Seven Herons Distillery – Label System</title>
<link href="https://fonts.googleapis.com/css2?family=Abril+Fatface&family=Archivo:wght@400;700;800&family=Special+Elite&family=Herr+Von+Muellerhoff&family=Old+Standard+TT&display=swap" rel="stylesheet">
<style>
  :root{
    --page:#f4f1ec;
    --paper:#ece7dc;
    --paper-shade:#ddd6c7;
    --ink:#141414;
    --accent-red:#d8312c;
    --gold:#d6a23e;
    --pink:#e58aa6;
    --pill:#d9d6d3;
    --band-plum:#3b1632;
    --band-plum-line:#55264a;
    --band-forest:#1f3418;
    --band-forest-line:#34502a;
  }
  *{box-sizing:border-box;margin:0;padding:0}
  html,body{width:1200px;height:1200px;overflow:hidden;background:var(--page)}
  .canvas{width:1200px;height:1200px;display:flex;justify-content:space-between;align-items:center;padding:0 20px}
  .label-set{width:570px;display:flex;flex-direction:column;align-items:center;gap:60px}

  /* upper square label */
  .front-label{position:relative;width:400px;height:400px;background:var(--paper);box-shadow:0 2px 6px rgba(0,0,0,.12)}
  .front-label .map-ground{position:absolute;inset:0;background:radial-gradient(circle at 40% 45%,var(--paper) 0%,var(--paper-shade) 100%)}
  .front-label .frame{position:absolute;inset:10px;border:2.5px solid var(--ink);display:flex;flex-direction:column;align-items:center;padding-top:34px}
  .lake-mark{width:110px;height:54px;border-radius:50%;background:var(--accent-red);opacity:.9;transform:rotate(-18deg);margin-left:40px}
  .wordmark{margin-top:18px;font-family:"Abril Fatface",serif;color:var(--ink);text-align:center;line-height:.86}
  .wordmark .wm-line{display:block;font-size:62px;letter-spacing:-2px}
  .wordmark .wm-sub{display:block;font-family:"Archivo",sans-serif;font-weight:400;font-size:18px;letter-spacing:3px;margin-top:8px}
  .batch-row{margin-top:30px;width:250px;display:flex;align-items:baseline;justify-content:space-between;border-bottom:1.5px solid var(--ink);padding-bottom:4px}
  .tiny-type{font-family:"Special Elite",monospace;font-size:8px;color:var(--ink)}
  .style-name{font-family:"Archivo",sans-serif;font-weight:800;font-size:22px;letter-spacing:2.5px;color:var(--accent-red)}
  .type-row{width:250px;display:flex;align-items:center;gap:8px;border-bottom:1.5px solid var(--ink);padding:2px 0 0}
  .type-row .caps{font-family:"Archivo",sans-serif;font-size:8px;letter-spacing:1px}
  .spirit-type{font-family:"Herr Von Muellerhoff",cursive;font-size:26px;color:var(--ink);line-height:1}

  /* lower band label */
  .band-label{position:relative;width:550px;height:190px;color:var(--gold)}
  .band-label .contour-ground{position:absolute;inset:0}
  .band-plum .contour-ground{background:linear-gradient(90deg,var(--band-plum),var(--band-plum-line) 50%,var(--band-plum))}
  .band-forest .contour-ground{background:linear-gradient(90deg,var(--band-forest),var(--band-forest-line) 50%,var(--band-forest))}
  .band-label .border{position:absolute;inset:14px 10px;border:1.5px solid var(--pink)}
  .tagline{position:absolute;top:40px;left:0;right:0;text-align:center;font-family:"Archivo",sans-serif;font-size:11px;letter-spacing:1.5px}
  .field-labels{position:absolute;top:78px;left:112px;right:132px;display:flex;justify-content:space-between;font-family:"Special Elite",monospace;font-size:9px}
  .abv{position:absolute;left:22px;top:96px;font-family:"Old Standard TT",serif;font-size:28px;line-height:1}
  .abv small{position:absolute;top:-10px;left:0;font-size:6px;letter-spacing:.5px}
  .info-pill{position:absolute;top:94px;left:96px;right:116px;height:32px;border-radius:16px;background:var(--pill);display:flex;align-items:center;justify-content:space-between;padding:0 18px;font-family:"Special Elite",monospace;color:var(--accent-red)}
  .info-pill .num{font-size:15px}
  .info-pill .date{font-size:11px;letter-spacing:2px}
  .info-pill .of{font-family:"Old Standard TT",serif;font-style:normal;font-size:9px;color:#555}
  .volume{position:absolute;right:22px;top:96px;font-family:"Old Standard TT",serif;font-size:28px;line-height:1}
</style>
</head>
<body>
<main class="canvas">

  <section class="label-set">
    <article class="front-label">
      <div class="map-ground" role="img" aria-label="Faint vintage street map of the lake area"></div>
      <div class="frame">
        <div class="lake-mark" role="img" aria-label="Red outline of Lac Vernisse"></div>
        <h1 class="wordmark"><span class="wm-line">SEVEN</span><span class="wm-line">HERONS</span><span class="wm-sub">DISTILLERY</span></h1>
        <div class="batch-row"><span class="tiny-type">Small</span><span class="style-name">TUBERIX</span><span class="tiny-type">Batch</span></div>
        <div class="type-row"><span class="caps">TYPE</span><span class="spirit-type">Straight Whiskey</span></div>
      </div>
    </article>
    <article class="band-label band-plum">
      <div class="contour-ground" role="img" aria-label="Topographic contour line pattern in plum tones"></div>
      <div class="border"></div>
      <p class="tagline">TRIPLE DISTILLED FROM LOCAL GRAINS</p>
      <div class="field-labels"><span>Batch N°</span><span>Date Bottled</span><span>Bottle N°</span></div>
      <p class="abv"><small>ALC/VOL</small>40%</p>
      <div class="info-pill"><span class="num">002</span><span class="date">24 / 11 / 2020</span><span class="num">07 <i class="of">of 19</i></span></div>
      <p class="volume">750ml</p>
    </article>
  </section>

  <section class="label-set">
    <article class="front-label">
      <div class="map-ground" role="img" aria-label="Faint vintage street map of the lake area"></div>
      <div class="frame">
        <div class="lake-mark" role="img" aria-label="Red outline of Lac Vernisse"></div>
        <h1 class="wordmark"><span class="wm-line">SEVEN</span><span class="wm-line">HERONS</span><span class="wm-sub">DISTILLERY</span></h1>
        <div class="batch-row"><span class="tiny-type">Small</span><span class="style-name">RED KITE</span><span class="tiny-type">Batch</span></div>
        <div class="type-row"><span class="caps">TYPE</span><span class="spirit-type">London Dry Gin</span></div>
      </div>
    </article>
    <article class="band-label band-forest">
      <div class="contour-ground" role="img" aria-label="Topographic contour line pattern in forest green tones"></div>
      <div class="border"></div>
      <p class="tagline">TRIPLE DISTILLED FROM LOCAL GRAINS</p>
      <div class="field-labels"><span>Batch N°</span><span>Date Bottled</span><span>Bottle N°</span></div>
      <p class="abv"><small>ALC/VOL</small>40%</p>
      <div class="info-pill"><span class="num">002</span><span class="date">24 / 11 / 2020</span><span class="num">07 <i class="of">of 19</i></span></div>
      <p class="volume">750ml</p>
    </article>
  </section>

</main>
</body>
</html>
```